Corporate Letter head and Microsoft Word Template

Brief
Design three clean, modern, professional corporate letter templates that include the BrightArc Corporation word-mark logo, company name and address and url. The designs should use one or more but no more than three tints/shades from our corporate colour pallet.
Templates should be produced in A4 and Letter formats as a Word file and should use Helvetica Now Display as the embedded font.
Design Preference:
Colour block designs, solid borders with flowing smooth lines, single side borders with connected header and footer, cut off or half page headers and footers are all acceptable.
Deliverables are:
1. Three graphic design files one for each brand logo colour and design
2. Three Word templates in 2 formats A4 and Letter
Enclosed are:
1. Three word mark logos with reverse versions of each, one for each primary brand colour.
2. BrightArc corporate colour pallet
3. BrightArc address and url
4. Helvetica Now Display font files

Target Market(s)

Professional Letter Writing to Suppliers, Customers and Authorities

Industry/Entity Type

High Tech

Font styles to use
Sans Serif
Other font styles liked:
• Helvetica Now Display

Requirements
Must have
• Clean, modern and effective design incorporating BrightArc Wordmark logo

```html
<!DOCTYPE html>
<html lang="en">
<head>
<meta charset="utf-8">
<title>BrightArc Letterhead</title>
<link href="https://fonts.googleapis.com/css2?family=Exo+2:wght@300;600;800&family=Source+Sans+3:wght@400&display=swap" rel="stylesheet">
<style>
  :root {
    --backdrop: #808080;
    --paper: #f6f3f3;
    --brand: #00aeef;
    --ink: #1c2230;
    --body-ink: #4a4a52;
  }
  html, body {
    margin: 0;
    padding: 0;
    width: 1072px;
    height: 1200px;
    overflow: hidden;
    background: var(--backdrop);
  }
  .letter {
    position: absolute;
    left: 199px;
    top: 132px;
    width: 682px;
    height: 962px;
    background: var(--paper);
  }
  .wordmark {
    position: absolute;
    left: 279px;
    top: 68px;
    margin: 0;
    font-family: "Exo 2", sans-serif;
    font-weight: 800;
    font-size: 34px;
    line-height: 40px;
    color: var(--brand);
    letter-spacing: -0.5px;
  }
  .header-rule {
    position: absolute;
    left: 450px;
    top: 73px;
    width: 1px;
    height: 54px;
    background: var(--brand);
  }
  .salutation {
    position: absolute;
    left: 68px;
    top: 269px;
    margin: 0;
    font-family: "Exo 2", sans-serif;
    font-weight: 600;
    font-size: 12.5px;
    color: var(--ink);
  }
  .letter-body {
    position: absolute;
    left: 67px;
    top: 319px;
    width: 550px;
    font-family: "Exo 2", sans-serif;
    font-weight: 300;
    font-size: 10px;
    line-height: 16.4px;
    color: var(--body-ink);
    text-align: justify;
  }
  .letter-body p { margin: 0 0 16.5px; }
  .closing {
    position: absolute;
    left: 67px;
    top: 664px;
    margin: 0;
    font-family: "Exo 2", sans-serif;
    font-weight: 300;
    font-size: 10px;
    color: var(--body-ink);
  }
  .signature {
    position: absolute;
    left: 68px;
    top: 708px;
    width: 88px;
    height: 36px;
  }
  .company-address {
    position: absolute;
    left: 68px;
    top: 878px;
    margin: 0;
    font-family: "Source Sans 3", sans-serif;
    font-style: normal;
    font-size: 12px;
    line-height: 14.4px;
    color: #3a3a3a;
  }
  .company-address .company-name { color: var(--brand); }
  .company-url {
    position: absolute;
    right: 68px;
    top: 907px;
    font-family: "Source Sans 3", sans-serif;
    font-size: 12px;
    color: var(--brand);
    text-decoration: none;
  }
</style>
</head>
<body>
  <main class="letter">
    <h1 class="wordmark">BrightArc</h1>
    <div class="header-rule"></div>

    <p class="salutation">Dear Mr. Hale,</p>

    <div class="letter-body">
      <p>Lorem ipsum dolor sit amet, consectetur adipiscing elit. Donec orci purus, luctus vitae dignissim eu, iaculis sed purus. Vivamus faucibus, ipsum nec aliquet viverra, leo mauris condimentum ligula, sit amet sagittis enim ligula quis arcu. Nam egestas tortor id nisi porttitor mattis. In tortor ante, ultricies in suscipit a, tempus non massa. Vivamus et auctor mi. Fusce vel massa nulla. Phasellus nec eros mauris, et scelerisque orci.</p>
      <p>Donec malesuada orci vitae nulla accumsan porta a id massa. Quisque accumsan iaculis magna sit amet fringilla. Maecenas consequat, magna eget tincidunt semper, odio nibh rutrum mi, id feugiat ante nisi eu risus. Vestibulum nunc orci, rhoncus a placerat in, ultricies in mi. Cras mattis varius eros, vel fringilla nisi suscipit eget. Quisque scelerisque sagittis nulla at porttitor.</p>
      <p>Sed id augue vitae urna euismod commodo aliquet a quam. Pellentesque arcu velit, cursus et malesuada ut, consequat et diam. Nullam erat sem, rhoncus id ullamcorper vitae, rhoncus et arcu. In ultricies ultricies nulla, ut rutrum nisi iaculis at. Donec eu magna a metus ornare faucibus. Fusce aliquet faucibus ultricies. Morbi semper, est id tincidunt gravida, sem arcu adipiscing lacus, ac bibendum nulla leo eu purus. Quisque nec diam sed risus consectetur a ccumsan quis quis nibh. Vestibulum id purus lorem.</p>
      <p>It is a long established fact that a reader will be distracted by the readable content of a page when looking at its layout. The point of using Lorem Ipsum is that it has a more-or-less normal distribution of letters, as opposed to using 'Content here, content here', making it look like readable English. Many desktop publishing packages</p>
    </div>

    <p class="closing">Sincerely,</p>
    <svg class="signature" role="img" aria-label="Handwritten signature" viewBox="0 0 88 36">
      <rect x="0" y="12" width="88" height="12" rx="6" fill="#d9d7da"/>
    </svg>

    <address class="company-address">
      <span class="company-name">BrightArc Corporation</span><br>
      4820 NW, Ridgeview Drive<br>
      Suite 300, Beaverton, OR 97006, United States
    </address>
    <a class="company-url" href="#">www.BrightArc.com</a>
  </main>
</body>
</html>
```